Fahrzeugbeschriftung  Corvanta CO.2.OTDI ELE 6 G und  Corvanta CO.2.OTDI AM beide Fahrzeugtypen sind Silber
Zielgruppe
www.belvoralarm.de
Neben unserer jahrzehntelangen Erfahrung besitzen wir außerdem die KfP-Anerkennung für Einbruchmeldeanlagen, sind GÜP-zertifiziert für Brandmeldeanlagen nach DIN 14675 und füllen ein zertifiziertes Qualitätsmanagement nach ISO 9001 mit Leben.
Wir sehen in uns nicht nur einen Handwerksbetrieb, sondern verstehen uns als Dienstleister der an Ihrer Seite als Ihr Unternehmen des Vertrauens fungieren möchte. Ob eine Alarmanlage für Ihren privaten Haushalt, Zutrittskontrolle für sensible Bereiche oder die komplette Videoüberwachung für Ihre Firma
Aufgabenstellung
Es soll nicht das ganze Auto beklebt werden.
Die Fahrzeuge sind Silber!!!!
Entweder beide seiten und hinten oder beide Seiten und Motorhaube. oder nur beide Seiten von einem Auto.
Es darf gern mit Grafiken und Icons gearbeitet werden.
Das Logo soll auffallen und im Gedächtnis bei dem Betrachter bleiben.
Auf die Telefonnummer kann verzichtet werden.
Gern hinter dem Firmennamen einfach ein ".de" setzen, um auch auf die Webseite zu verweisen.
Es soll einfach klar ersichtlich sein, was die Firma Belvor Alarm anbietet und sich mit Logo der Firma ins Gedächtnis brennen.
PDF Dateien einfach mal anschauen - glaube die sind zur Orientierung sehr gut

```html
<!DOCTYPE html>
<html lang="de">
<head>
<meta charset="utf-8">
<title>Belvor Alarm – Fahrzeugbeschriftung</title>
<link rel="stylesheet" href="https://fonts.googleapis.com/css2?family=Roboto+Condensed:wght@700&display=swap">
<style>
  :root {
    --brand-blue: #1f4f9a;
    --brand-red: #e0352b;
    --brand-grey: #8d9299;
    --vehicle-silver: #f4f5f6;
  }
  * { margin: 0; padding: 0; box-sizing: border-box; }
  html, body {
    width: 1200px;
    height: 751px;
    overflow: hidden;
    background: var(--vehicle-silver);
  }
  .livery {
    width: 1200px;
    height: 751px;
    display: flex;
    align-items: center;
    justify-content: center;
  }
  .livery-panel {
    display: grid;
    grid-template-columns: 300px auto;
    column-gap: 40px;
    row-gap: 16px;
    align-items: center;
    font-family: "Roboto Condensed", sans-serif;
    font-weight: 700;
  }
  .brand-dot {
    grid-column: 1;
    grid-row: 1;
    justify-self: end;
    width: 96px;
    height: 96px;
    border-radius: 50%;
    background: var(--brand-red);
  }
  .brand-name {
    grid-column: 2;
    grid-row: 1;
    font-size: 104px;
    line-height: 1;
    color: var(--brand-blue);
    white-space: nowrap;
  }
  .tagline {
    grid-column: 2;
    grid-row: 2;
    font-size: 32px;
    letter-spacing: 1px;
    color: var(--brand-grey);
    text-transform: uppercase;
  }
  .service-icons {
    grid-column: 1;
    grid-row: 3;
    display: flex;
    justify-content: space-between;
  }
  .service-icon { width: 56px; height: 56px; fill: var(--brand-red); }
  .phone {
    grid-column: 2;
    grid-row: 3;
    font-size: 42px;
    letter-spacing: 1px;
    color: var(--brand-blue);
  }
</style>
</head>
<body>
<main class="livery">
  <section class="livery-panel">
    <span class="brand-dot" aria-hidden="true"></span>
    <p class="brand-name">Belvor Alarm</p>
    <p class="tagline">Sicherheitstechnik</p>

    <div class="service-icons" aria-label="Leistungen">
      <svg class="service-icon" viewBox="0 0 52 52" role="img" aria-label="Alarmanlage">
        <rect x="18" y="18" width="16" height="22" rx="8"/>
        <rect x="14" y="38" width="24" height="5" rx="1"/>
        <path d="M10 16a20 20 0 0 0 0 24l3-2a16 16 0 0 1 0-20z M42 16a20 20 0 0 1 0 24l-3-2a16 16 0 0 0 0-20z"/>
      </svg>
      <svg class="service-icon" viewBox="0 0 52 52" role="img" aria-label="Brandschutz">
        <path d="M26 4c2 10 14 14 14 28a14 14 0 0 1-28 0c0-8 5-12 7-18 2 5 4 7 6 8 2-6 1-12 1-18z"/>
      </svg>
      <svg class="service-icon" viewBox="0 0 52 52" role="img" aria-label="Videoüberwachung">
        <path d="M6 14l30 10-5 10-28-10z"/>
        <path d="M36 27l8 3-2 5-8-3z"/>
        <rect x="18" y="32" width="4" height="10"/>
        <rect x="8" y="40" width="16" height="4"/>
      </svg>
      <svg class="service-icon" viewBox="0 0 52 52" role="img" aria-label="Technischer Service">
        <path d="M22 4h8l1 6 5 2 5-4 6 6-4 5 2 5 6 1v8l-6 1-2 5 4 5-6 6-5-4-5 2-1 6h-8l-1-6-5-2-5 4-6-6 4-5-2-5-6-1v-8l6-1 2-5-4-5 6-6 5 4 5-2zM26 18a8 8 0 1 0 0 16a8 8 0 1 0 0-16z" fill-rule="evenodd"/>
      </svg>
    </div>

    <p class="phone">4180-306-519 7</p>
  </section>
</main>
</body>
</html>
```